Takeout Menu Design for Japanese Restaurant.

I need to have a takeout menu designed for my newly opened restaurant. I uploaded a word file with very specific information on the project overall. Please download it to understand the scope.
Updates

Hello designers,

I have posted an archive containing some updated files. I will provide the explanation for each piece below:

1. The PDF and the 2.jpg represent the photos that are supposed to appear on the Teppanyaki panel. I do not know how to extract the photo from the PDF so I uploaded it as is. There is no higher resolution version of 2.jpg. If useable, choose one that is more appropriate for the menu, if not, use a stock photo with similar configuration as presented in the photos.

2. The screenshot is a mock up of how I want the map to represent. The town is large so clearly marking the Brell-Mart is a priority. Obviously, I want the final map to look much better than the screenshot I uploaded. You can simply grap the Pindo Charts file I uploaded in the previous archive and clean it up of irrelevant information such as other businesses, buildings and texts and colour in where the Brell-Mart is supposed to be blue and preferably use the Brellmart symbol. Also, please make where the restaurant is more apparent, not just a location marker A. 

3. The Teppanyaki Directive.docx contains text that is supposed to appear on the Teppanyaki panel, superimposing the photo, which is supposed to cover most, if not all of the panel. I think it is pretty clear, if not, please specify which areas you need explained. 

Industry/Entity Type

Restaurant

Requirements
Must have
• - Restaurant name & logo.
- On the front stating a new restaurant or grand opening (Must be apparent.)
- Hours of operation.
- Contact information (phone number and fax.)
- Website address.
- Stylized map showing approximate address of establishment.
- Specific address of establishment
- Menu items.

- The flyer is 11 X 17. The design templates for specific measurements are provided.
- Double sided (6 panels in all. Roll fold.)

```html
<!DOCTYPE html>
<html lang="en">
<head>
<meta charset="utf-8">
<title>Kiro Takeout Menu – Inside</title>
<link href="https://fonts.googleapis.com/css2?family=Roboto+Condensed:ital,wght@0,300;0,400;0,700;1,300;1,400&display=swap" rel="stylesheet">
<style>
:root{
  --ink:#2a2a2a;
  --muted:#555;
  --orange:#e5862c;
  --green:#8ea53d;
  --olive:#8a9a3a;
  --blue:#5f8099;
  --rule:#b9b9b9;
  --paper:#ffffff;
}
*{box-sizing:border-box;margin:0;padding:0}
html,body{width:1200px;height:776px;overflow:hidden;background:var(--paper)}
body{position:relative;font-family:"Roboto Condensed",Arial,sans-serif;color:var(--ink)}
.col{position:absolute;overflow:hidden}
.heading{font-weight:300;font-size:24px;line-height:1;text-transform:uppercase;letter-spacing:.3px;margin-bottom:4px;white-space:nowrap}
.heading small{font-size:10px;text-transform:none;letter-spacing:0;vertical-align:middle;margin-left:4px}
.subheading{font-weight:300;font-size:17px;line-height:1;margin:5px 0 3px}
.orange{color:var(--orange)} .green{color:var(--green)} .blue{color:var(--blue)} .olive{color:var(--olive)}
.item{margin-bottom:4px}
.line{display:flex;align-items:baseline;font-size:9.6px;line-height:11px;white-space:nowrap}
.line i{flex:1;border-bottom:1px dotted #777;margin:0 2px;transform:translateY(-2px)}
.desc{font-style:italic;font-weight:300;font-size:6.6px;line-height:7.6px;color:var(--muted)}
.twocol{display:flex;gap:12px}
.twocol>div{flex:1;min-width:0}
.rows .item{margin-bottom:4px}
.photo{position:absolute;border-radius:2px}
.divider{position:absolute;background:var(--rule)}
</style>
</head>
<body>

<!-- LEFT PANEL -->
<section class="col" style="left:18px;top:14px;width:385px;height:298px">
  <h2 class="heading orange">Appetizers</h2>
  <div class="twocol">
    <div>
      <div class="item"><p class="line">Edamame (A1)<i></i>$4.95</p><p class="desc">Tender soybeans boiled in their shells, slightly salted.</p></div>
      <div class="item"><p class="line">Agedashi Tofu (A2)<i></i>$5.95</p><p class="desc">Tofu delicately deep-fried and served with tentsuyu sauce and topped with scallion.</p></div>
      <div class="item"><p class="line">Gyoza (A3)<i></i>$6.95</p><p class="desc">Japanese dumplings delicately pan-fried and served with house spicy dip.</p></div>
      <div class="item"><p class="line">Tuna Tataki (A4)<i></i>$12.95</p><p class="desc">Seared sliced albacore tuna with daikon radish and chili oil. Finished with roasted sesame and house ponzu sauce.</p></div>
      <div class="item"><p class="line">Yam "Bam-Bam" Fried (A5)<i></i>$11.95</p><p class="desc">Fried yam topped with diced salmon, mango, avocado and house spicy sauce.</p></div>
      <div class="item"><p class="line">Salmon Yuke (A6)<i></i>$8.95</p><p class="desc">Diced salmon mixed with spicy sauce, tempura crunch and topped with scallion.</p></div>
      <div class="item"><p class="line">Beef Tataki (A7)<i></i>$11.95</p><p class="desc">Seared sliced steak, served with ponzu sauce and topped with scallions.</p></div>
      <div class="item"><p class="line">BBQ Karubi (A8)<i></i>$11.95</p><p class="desc">Grilled beef short ribs marinated with sake, sweet soy sauce, garlic and pepper.</p></div>
      <div class="item"><p class="line">Avocado Lover (A9)<i></i>$7.95</p><p class="desc">Avocado tempura topped with eel sauce, mayonnaise and scallion.</p></div>
    </div>
    <div>
      <div class="item"><p class="line">Ebi Mayo (A10)<i></i>$11.95</p><p class="desc">7 lightly battered tiger prawns deep-fried and served with spicy mayonnaise.</p></div>
      <div class="item"><p class="line">Chicken (2) or Beef Skewers (2) (A11)<i></i>$6.95</p><p class="desc">Japanese style, served with our house teriyaki sauce and topped with sesame seeds and green onions.</p></div>
      <div class="item"><p class="line">Ika Yaki (A12)<i></i>$8.95</p><p class="desc">BBQ squid with teriyaki sauce.</p></div>
      <div class="item"><p class="line">Deep Fried Wontons (A13)<i></i>$5.95</p><p class="desc">6 wontons are fried golden crisp and served with our house dipping.</p></div>
      <div class="item"><p class="line">Deep Fried Spring Rolls (A14)<i></i>$6.95</p><p class="desc">5 spring rolls are fried to a golden crisp and served with plum sauce.</p></div>
      <div class="item"><p class="line">Seafood Skewers (2) (A15)<i></i>$6.95</p><p class="desc">Japanese style, served with our house teriyaki sauce and topped with sesame seeds and green onions.</p></div>
    </div>
  </div>
</section>
<div class="photo" role="img" aria-label="Golden fried spring rolls with dipping sauce on a leaf" style="left:205px;top:212px;width:195px;height:92px;background:linear-gradient(135deg,#f4f1ea 0%,#e4c48a 45%,#c98a3a 70%,#f2efe8 100%)"></div>

<section class="col" style="left:18px;top:314px;width:385px;height:72px">
  <h2 class="heading green">Tempura <small>Deep-fried lightly battered shrimp or vegetables, served with Ponzu sauce.</small></h2>
  <div class="twocol">
    <div>
      <div class="item"><p class="line">Assorted (B1)<i></i>$13.95</p><p class="desc">4 tiger prawns and 6 pieces of a variety of vegetables.</p></div>
      <div class="item"><p class="line">Prawn (B2)<i></i>$11.95</p><p class="desc">7 large tiger prawns.</p></div>
    </div>
    <div>
      <div class="item"><p class="line">Vegetable (B3)<i></i>$7.95</p><p class="desc">7 pieces of a variety of vegetables.</p></div>
      <div class="item"><p class="line">Yam (B4)<i></i>$6.95</p><p class="desc">6 pieces of sweet potatoes.</p></div>
    </div>
  </div>
</section>

<section class="col" style="left:18px;top:390px;width:385px;height:96px">
  <h2 class="heading blue">Soup and Salad</h2>
  <div class="twocol">
    <div>
      <div class="item"><p class="line">House Green Salad (C1)<i></i>$5.95</p><p class="desc">Cherry tomatoes, cucumbers, and avocados on a bed of greens. Served with our house made ginger dressing.</p></div>
      <div class="item"><p class="line">Gomae Salad (C2)<i></i>$5.95</p><p class="desc">Blanched spinach served with our house made sweet sesame dressing.</p></div>
    </div>
    <div class="rows">
      <div class="item"><p class="line">Seaweed Salad (C3)<i></i>$6.95</p></div>
      <div class="item"><p class="line">Miso Soup (C4)<i></i>$2.50</p></div>
      <div class="item"><p class="line">Medium Wor Wonton Soup (C5)<i></i>$8.95</p></div>
      <div class="item"><p class="line">Large Wor Wonton Soup (C6)<i></i>$12.95</p></div>
    </div>
  </div>
</section>

<section class="col" style="left:18px;top:488px;width:385px;height:288px">
  <h2 class="heading green">Sashimi <small>Raw meat of fish and other seafood, served in bite sized pieces.</small></h2>
  <div class="item"><p class="line">Hokkigai (D1)<i></i>(3pcs) $5.95<i></i>(8pcs) $14.95</p><p class="desc">Surf Clam</p></div>
  <div class="item"><p class="line">Smoked Salmon (D2)<i></i>(3pcs) $5.95<i></i>(8pcs) $14.95</p><p class="desc">Salmon (D3) – (3)$5.95 – (8)$14.95</p></div>
  <div class="item"><p class="line">Albacore Tuna (D4)<i></i>(3pcs) $5.95<i></i>(8pcs) $14.95</p></div>
  <div class="item"><p class="line">Tai (D5)<i></i>(3pcs) $5.95<i></i>(8pcs) $14.95</p><p class="desc">Red Snapper</p></div>
  <div class="item"><p class="line">Saba (D6)<i></i>(3pcs) $6.50<i></i>(8pcs) $15.95</p><p class="desc">Mackerel</p></div>
  <div class="item"><p class="line">Tako (D7)<i></i>(3pcs) $6.50<i></i>(8pcs) $15.95</p><p class="desc">Octopus</p></div>
  <div class="item"><p class="line">Spicy Tuna (D8)<i></i>(3pcs) $6.50<i></i>(8pcs) $15.95</p></div>
  <div class="item"><p class="line">Toro (D9)<i></i>(3pcs) $6.95<i></i>(8pcs) $16.95</p><p class="desc">Fatty Tuna Belly</p></div>
  <div class="item"><p class="line">Hamachi (D10)<i></i>(3pcs) $6.95<i></i>(8pcs) $16.95</p><p class="desc">Yellowtail</p></div>
  <div class="item"><p class="line">Assorted (D11)<i></i>(14pcs) $25.95</p></div>
  <div class="item"><p class="line">Tuna/Salmon (D12)<i></i>(8pcs) $14.95</p></div>
  <div class="item"><p class="line">Combo A (D13)<i></i>$18.95</p><p class="desc">2 salmon, 2 toro, 2 hamachi, 3 tuna.</p></div>
  <div class="item"><p class="line">Combo B (D14)<i></i>$12.95</p><p class="desc">2 wild salmon, 3 tuna.</p></div>
</section>

<!-- MIDDLE PANEL -->
<section class="col" style="left:420px;top:16px;width:384px;height:240px">
  <h2 class="heading green">Nigiri <small>Made from topping vinaigrette rice with a thin slice of fish, egg or seafood.</small></h2>
  <p class="desc" style="font-size:9px;line-height:10px;font-style:normal;color:var(--green);margin:-2px 0 5px">Comes in servings of 2.</p>
  <div class="twocol">
    <div>
      <div class="item"><p class="line">Inari (E1)<i></i>$4.00</p><p class="desc">Sweet bean curd.</p></div>
      <div class="item"><p class="line">Tamago (E2)<i></i>$4.00</p><p class="desc">Sweet egg.</p></div>
      <div class="item"><p class="line">Salmon (E3)<i></i>$4.95</p></div>
      <div class="item"><p class="line">Tuna (E4)<i></i>$4.95</p></div>
      <div class="item"><p class="line">Masago (E5)<i></i>$4.95</p><p class="desc">Smelt roe.</p></div>
      <div class="item"><p class="line">Hokkigai (E6)<i></i>$4.95</p><p class="desc">Surf clam.</p></div>
      <div class="item"><p class="line">Ebi (E7)<i></i>$4.95</p><p class="desc">Cooked prawn.</p></div>
      <div class="item"><p class="line">Smoked Salmon (E8)<i></i>$4.95</p></div>
      <div class="item"><p class="line">Tako (E9)<i></i>$5.50</p><p class="desc">Octopus</p></div>
      <div class="item"><p class="line">Tobiko (E10)<i></i>$5.50</p><p class="desc">Flying fish roe.</p></div>
    </div>
    <div>
      <div class="item"><p class="line">Saba (E11)<i></i>$5.50</p><p class="desc">Mackerel.</p></div>
      <div class="item"><p class="line">Ika (E12)<i></i>$5.50</p><p class="desc">Cuttlefish.</p></div>
      <div class="item"><p class="line">Spicy Tuna (E13)<i></i>$5.50</p></div>
      <div class="item"><p class="line">Spicy Salmon (E14)<i></i>$5.50</p></div>
      <div class="item"><p class="line">Toro (E15)<i></i>$5.95</p><p class="desc">Fatty tuna belly.</p></div>
      <div class="item"><p class="line">Chopped Scallop (E16)<i></i>$5.95</p></div>
      <div class="item"><p class="line">Ikura (E17)<i></i>$5.95</p><p class="desc">Salmon roe.</p></div>
      <div class="item"><p class="line">Unagi (E18)<i></i>$5.95</p><p class="desc">BBQ eel.</p></div>
      <div class="item"><p class="line">Hotate (E19)<i></i>$5.95</p><p class="desc">Scallop.</p></div>
      <div class="item"><p class="line">Hamachi (E20)<i></i>$5.95</p><p class="desc">Yellowtail.</p></div>
    </div>
  </div>
</section>

<section class="col" style="left:420px;top:256px;width:384px;height:106px">
  <h2 class="heading blue">Rice Bowls <small>All rice bowls are served with miso soup.</small></h2>
  <div class="twocol rows">
    <div>
      <div class="item"><p class="line">BBQ Eel (H1)<i></i>$14.95</p></div>
      <div class="item"><p class="line">Teriyaki Chicken (H2)<i></i>$12.95</p></div>
      <div class="item"><p class="line">Teriyaki Beef (H3)<i></i>$12.95</p></div>
      <div class="item"><p class="line">Tempura and Teriyaki Chicken</p><p class="line">or Beef (H4)<i></i>$13.95</p></div>
    </div>
    <div>
      <div class="item"><p class="line">Chicken Katsu (H5)<i></i>$12.95</p></div>
      <div class="item"><p class="line">Teriyaki Prawn (H6)<i></i>$13.95</p></div>
      <div class="item"><p class="line">Teriyaki Tofu (H7)<i></i>$11.95</p></div>
      <div class="item"><p class="line">Red Snapper (H8)<i></i>$13.95</p></div>
      <div class="item"><p class="line">Teriyaki Salmon (H9)<i></i>$14.95</p></div>
    </div>
  </div>
</section>

<!-- RIGHT PANEL -->
<section class="col" style="left:818px;top:16px;width:378px;height:142px">
  <h2 class="heading blue">Udon <small>Thick noodles made from wheat flour served in soup.</small></h2>
  <div class="item"><p class="line">Chicken with Tempura (J1)<i></i>$13.95</p><p class="desc">Chicken, fish cake, boiled egg, shrimp tempura, mushrooms and assorted vegetables.</p></div>
  <div class="item"><p class="line">Chicken (J2)<i></i>$11.95</p><p class="desc">Chicken, fish cake, boiled egg and assorted vegetables.</p></div>
  <div class="item"><p class="line">Beef with Tempura (J3)<i></i>$13.95</p><p class="desc">Shaved beef, fish cake, boiled egg, shrimp tempura and assorted vegetables.</p></div>
  <div class="item"><p class="line">Beef (J4)<i></i>$11.95</p><p class="desc">Shaved beef, fish cake, boiled egg and assorted vegetables.</p></div>
  <div class="item"><p class="line">Stir Fried (J5)<i></i>$11.95</p><p class="desc">Stir fried udon with your choice of chicken, beef, seafood, or vegetables.</p></div>
</section>

<section class="col" style="left:818px;top:158px;width:178px;height:205px">
  <h2 class="heading green">Boats <small style="margin-left:2px">All boats are served</small></h2>
  <p style="font-size:10px;color:var(--green);font-weight:300;margin:-3px 0 4px;white-space:nowrap">with miso soup and house salad.</p>
  <div class="item"><p class="line">Kiro Special (L1)<i></i>$16.95</p><p class="desc">4 oz. New York steak with mushrooms and onions, chicken karaage, 4 assorted tempura, 3 dynamite roll and 3 dynamite roll.</p></div>
  <div class="item"><p class="line">Spicy (L2)<i></i>$16.95</p><p class="desc">3 spicy tuna roll, 3 spicy salmon roll, 3 spicy gyoza, 4 assorted tempura and 4 spicy prawn.</p></div>
  <div class="item"><p class="line">Deluxe (L3)<i></i>$17.95</p><p class="desc">Chicken or beef teriyaki, 2 tuna sashimi, 2 salmon sashimi, 3 house roll and 4 assorted tempura.</p></div>
  <div class="item"><p class="line">BBQ Eel and Sashimi (L4)<i></i>$17.95</p><p class="desc">BBQ eel on rice, 2 tuna sashimi, 2 salmon sashimi, 4 assorted tempura, 2 house roll and 2 dynamite roll.</p></div>
  <div class="item"><p class="line">Nigiri sushi and Sashimi (L5)<i></i>$17.95</p><p class="desc">2 tuna sashimi, 2 salmon sashimi, 1 tuna nigiri, 1 salmon nigiri, 1 egg nigiri, 3 house roll, 3 dynamite roll and 2 fruits.</p></div>
</section>
<div class="photo" role="img" aria-label="Wooden sushi boat loaded with sashimi, rolls and garnish" style="left:1002px;top:150px;width:194px;height:98px;background:linear-gradient(160deg,#ffffff 0%,#e9b87a 30%,#b0592e 55%,#6e3a1e 75%,#ffffff 100%)"></div>
<section class="col" style="left:1005px;top:253px;width:190px;height:110px">
  <div class="item"><p class="line">Sushi and Maki (L6)<i></i>$43.95</p><p class="desc">12 nigiri, 12 tuna roll, 12 salmon roll, 12 shrimp tempura roll and 12 shrimp tempura roll.</p></div>
  <div class="item"><p class="line">Kitchen (L7)<i></i>$41.95</p><p class="desc">8 oz. New York steak with mushroom and onion, chicken or beef teriyaki, BBQ Karubi, 4 assorted tempura, 4 gyoza, 2 spring rolls and rice.</p></div>
  <div class="item"><p class="line">House (L8)<i></i>$45.95</p><p class="desc">4 sashimi, 6 nigiri, chicken or beef teriyaki, 10 oz. Rib eye steak, 4 assorted tempura, 4 gyoza, 2 spring rolls and rice.</p></div>
</section>

<div class="divider" style="left:420px;top:364px;width:776px;height:1px"></div>

<!-- MAKI -->
<h2 class="heading olive" style="position:absolute;left:420px;top:373px">Maki <small>A variety of sushi where ingredients are rolled into a cylinder and then cut into bite sized pieces.</small></h2>

<section class="col" style="left:420px;top:398px;width:185px;height:378px">
  <h3 class="subheading olive" style="margin-top:0">Classic Maki</h3>
  <div class="item"><p class="line">Philadelphia (G1)<i></i>$10.95</p><p class="desc">Smoked salmon, scallion, cucumber and cream cheese.</p></div>
  <div class="item"><p class="line">California (G2)<i></i>$6.95</p><p class="desc">Crab, avocado and mayonnaise.</p></div>
  <div class="item"><p class="line">BC (G3)<i></i>$6.95</p><p class="desc">BBQ salmon skin, cucumber and teriyaki sauce.</p></div>
  <div class="item"><p class="line">Alaska (G4)<i></i>$8.95</p><p class="desc">Crab, smoked salmon, avocado and mayonnaise.</p></div>
  <div class="item"><p class="line">Dynamite (G5)<i></i>$8.95</p><p class="desc">Prawn tempura, cucumber, avocado, lettuce and eel sauce.</p></div>
  <div class="item"><p class="line">Chopped Scallop (G6)<i></i>$7.95</p><p class="desc">Scallop, smelt roe, avocado and mayonnaise.</p></div>
  <div class="item"><p class="line">Salmon (G7)<i></i>$5.95</p></div>
  <div class="item"><p class="line">Tuna (G8)<i></i>$5.95</p></div>
  <div class="item"><p class="line">Negi Toro (G9)<i></i>$7.95</p><p class="desc">Fatty tuna belly and scallion.</p></div>
  <div class="item"><p class="line">Tuna Crunch (G10)<i></i>$7.95</p><p class="desc">Tuna, tempura flakes and mayonnaise.</p></div>
  <div class="item"><p class="line">Unagi (G11)<i></i>$8.95</p><p class="desc">BBQ eel, cucumber and eel sauce.</p></div>
  <div class="item"><p class="line">Chicken Teriyaki (G12)<i></i>$7.95</p><p class="desc">Grilled chicken, cucumber, lettuce and teriyaki sauce.</p></div>
  <div class="item"><p class="line">Spider (G13)<i></i>$8.95</p><p class="desc">Lightly battered soft shell crab, fish roe, avocado, cucumber, lettuce and eel sauce.</p></div>
  <h3 class="subheading olive">Fruity Maki</h3>
  <div class="item"><p class="line">California Mango (G14)<i></i>$6.95</p><p class="desc">Crab, mango, cucumber, and mayonnaise.</p></div>
  <div class="item"><p class="line">Mango Tuna (G15)<i></i>$6.95</p><p class="desc">Tuna, mango, and avocado.</p></div>
</section>

<section class="col" style="left:615px;top:398px;width:190px;height:378px">
  <div class="item"><p class="line">Electric Banana (G16)<i></i>$12.95</p><p class="desc">BBQ eel, avocado, banana tempura, and eel sauce.</p></div>
  <div class="item"><p class="line">Fancy (G17)<i></i>$11.95</p><p class="desc">Prawn tempura, mango, avocado, and cream cheese. Wrapped in soybean sheet.</p></div>
  <div class="item"><p class="line">Reggae Bob (G18)<i></i>$11.95</p><p class="desc">Tuna, mango, avocado and wasabi mayonnaise.</p></div>
  <div class="item"><p class="line">Greenie (G19)<i></i>$12.95</p><p class="desc">Prawn tempura and mango. Wrapped in avocado.</p></div>
  <h3 class="subheading olive">Kiro Desire Maki</h3>
  <div class="item"><p class="line">Orange Crush (G20)<i></i>$12.95</p><p class="desc">Crab, salmon, asparagus, avocado, cream cheese and spicy mayonnaise.</p></div>
  <div class="item"><p class="line">Happy Eel (G21)<i></i>$13.95</p><p class="desc">BBQ eel, crab, masago, scallion and cream cheese. Lightly battered and deep-fried. Decorated with spicy mayonnaise and eel sauce.</p></div>
  <div class="item"><p class="line">Volcano (G22)<i></i>$13.95</p><p class="desc">Tuna, scallop and avocado. Deep fried and served on a bed of crabmeat with spicy sauce.</p></div>
  <div class="item"><p class="line">Mexi Cali (G23)<i></i>$12.95</p><p class="desc">California rolls with salsa, tomatoes, avocado and diced salmon. Served with spicy sauce.</p></div>
  <div class="item"><p class="line">Spicy Trio (G24)<i></i>$13.95</p><p class="desc">Spicy salmon, spicy tuna, yellow tail, avocado and cream cheese. Lightly battered and deep-fried. Topped with spicy mayonnaise.</p></div>
  <div class="item"><p class="line">Devil's Roll (G25)<i></i>$13.95</p><p class="desc">Prawn tempura, tuna, cucumber, avocado and spicy sauce.</p></div>
  <div class="item"><p class="line">69 (G26)<i></i>$14.95</p><p class="desc">Crab, salmon, BBQ eel and avocado. Decorated with wasabi mayonnaise.</p></div>
  <div class="item"><p class="line">Spicy Salmon (G27)<i></i>$6.95</p><p class="desc">Salmon, cucumber and spicy sauce.</p></div>
</section>

<section class="col" style="left:818px;top:398px;width:182px;height:378px">
  <div class="item"><p class="line">Spicy Tuna (G28)<i></i>$6.95</p><p class="desc">Tuna, cucumber and spicy sauce.</p></div>
  <div class="item"><p class="line">Spicy Salmon Crunch (G29)<i></i>$8.95</p><p class="desc">Salmon, tempura flakes and spicy sauce.</p></div>
  <div class="item"><p class="line">Red Ninja (G30)<i></i>$12.95</p><p class="desc">Spicy tuna and tempura flakes, tempura salmon and tempura avocado. Decorated with masago and mayonnaise.</p></div>
  <div class="item"><p class="line">White Ninja (G31)<i></i>$12.95</p><p class="desc">Spicy tuna and tempura flakes. Topped with avocado. Decorated with eel sauce and mayonnaise.</p></div>
  <div class="item"><p class="line">Tiger's Eye (G32)<i></i>$12.95</p><p class="desc">Salmon, jalapeno and cream cheese. Lightly battered tempura style and topped with wasabi mayonnaise.</p></div>
  <div class="item"><p class="line">Las Vegas (G33)<i></i>$13.95</p><p class="desc">BBQ eel, crab, avocado and cream cheese. Tempura style and served spicy mayonnaise.</p></div>
  <h3 class="subheading olive">Creative Maki</h3>
  <div class="item"><p class="line">Found Fishy (G34)<i></i>$13.95</p><p class="desc">Soft shell crab tempura, asparagus and avocado topped with seared salmon and unagi sauce.</p></div>
  <div class="item"><p class="line">Crunchy (G35)<i></i>$13.95</p><p class="desc">Smoked salmon, crab and cucumber topped with smelt fish roe and tempura flakes.</p></div>
  <div class="item"><p class="line">Dragon (G36)<i></i>$14.95</p><p class="desc">Prawn tempura, avocado and cucumber wrapped over BBQ eel tempura, with eel sauce and mayonnaise.</p></div>
  <div class="item"><p class="line">Captain Crisp (G37)<i></i>$10.95</p><p class="desc">Deep-fried breaded California rolls decorated with eel sauce and mayonnaise.</p></div>
  <div class="item"><p class="line">Tuna Tataki Roll (G38)<i></i>$12.95</p><p class="desc">California rolls topped with seared tuna and unagi sauce.</p></div>
  <div class="item"><p class="line">Rainbow (G39)<i></i>$13.95</p><p class="desc">Crab and cucumber wrapped over salmon, tuna and avocado.</p></div>
</section>

<section class="col" style="left:1008px;top:398px;width:188px;height:268px">
  <div class="item"><p class="line">Miss Porky (G40)<i></i>$12.95</p><p class="desc">Crispy bacon, scallop, and asparagus topped with fish roe and unagi sauce.</p></div>
  <div class="item"><p class="line">Japanese Cowboy (G41)<i></i>$10.95</p><p class="desc">Beef teriyaki, asparagus and lettuce with a touch of teriyaki sauce.</p></div>
  <h3 class="subheading olive">Vegetable Maki</h3>
  <div class="item"><p class="line">Sunshine (G42)<i></i>$8.95</p><p class="desc">Mango, avocado and cream cheese. Wrapped in soybean sheets.</p></div>
  <div class="item"><p class="line">Buddha (G43)<i></i>$7.95</p><p class="desc">Yam tempura, asparagus, avocado and lettuce.</p></div>
  <div class="item"><p class="line">Mango Paradise (G44)<i></i>$7.95</p><p class="desc">Mango, avocado, inari and cucumber.</p></div>
  <div class="item"><p class="line">Banana (G45)<i></i>$8.95</p><p class="desc">Banana tempura, avocado and cream cheese. Topped with miso sauce.</p></div>
  <div class="item"><p class="line">Vegetable (G46)<i></i>$7.95</p><p class="desc">Avocado, cucumber, carrot, asparagus, red pepper and lettuce.</p></div>
  <div class="item"><p class="line">Avocado (G47)<i></i>$5.95</p><p class="desc">Avocados.</p></div>
  <div class="item" style="width:88px"><p class="line">Yam (G48)<i></i>$5.95</p><p class="desc">Yam.</p></div>
  <div class="item" style="width:88px"><p class="line">Kappa (G49)<i></i>$4.95</p><p class="desc">Cucumber.</p></div>
</section>
<div class="photo" role="img" aria-label="Sushi rolls topped with seared salmon and sauce on a white plate" style="left:1100px;top:660px;width:100px;height:116px;background:linear-gradient(150deg,#ffffff 0%,#eef0f2 35%,#f0b48a 60%,#c8703f 80%,#e9ecef 100%)"></div>

</body>
</html>
```